New website for Ember Crew Company

Ember Crew Company is a new start up, with a focus on rebuilding business software on Orbitra.com (Quillvane platform). Next to this we are specialised in implementing Quillvane apps like Plumtrek and Marbleloft.
The new website should be truly business oriented reflecting both the App development on Orbitra.Com and the Consultancy part of implementing Quillvane apps. Ideally the website is build on top of Joomla or Drupal as CMS.
Updates

Reason: I have reduced my request to 1 webdesign for EmberCrew Company. It should be a powerfull but simple website like: www.kelvatio.com www.plumtrek.com I would like to have it running on Joomla or Drupal

Target Market(s)

Medium sized companies (50-500 employees) for the app rebuilding. Large companies for the consultancy part for implementation of apps

Industry/Entity Type

Business Software

Font styles to use
Sans Serif

Requirements
Must have
• Joomla / Drupal compatible. Easy to update content design with full bleed images and responsive design. Special area to show case reference projects

```html
<!DOCTYPE html>
<html lang="en">
<head>
<meta charset="utf-8">
<title>Ember Crew Company</title>
<link href="https://fonts.googleapis.com/css2?family=Arimo:wght@400;700&display=swap" rel="stylesheet">
<style>
:root{
  --blue:#1a9ad6;
  --blue-dark:#1282bb;
  --ink:#222;
  --text:#555;
  --muted:#888;
  --line:#e3e3e3;
  --soft:#f2f2f2;
  --footer:#1d1f21;
  --footer-bottom:#141516;
  --white:#fff;
}
*{box-sizing:border-box;margin:0;padding:0}
html,body{width:1200px;height:2308px;overflow:hidden}
body{font-family:"Arimo",Arial,sans-serif;color:var(--text);background:var(--white);position:relative}
.wrap{position:absolute;left:185px;width:830px}

/* Hero */
.hero{position:absolute;left:0;top:0;width:1200px;height:487px;overflow:hidden}
.hero-photo{position:absolute;inset:0;background:linear-gradient(90deg,#e9f3f9 0%,#d4e7f3 35%,#9fb9cf 62%,#3e5a78 80%,#dfe9f0 100%)}
.topbar{position:absolute;left:0;top:0;width:1200px;height:72px;background:linear-gradient(180deg,rgba(26,154,214,.9),rgba(26,154,214,.55))}
.brand{position:absolute;left:185px;top:22px;display:flex;align-items:center;gap:8px;color:var(--white);font-size:19px;font-weight:700;white-space:nowrap}
.brand-dot{width:24px;height:24px;border-radius:50%;background:var(--white)}
.nav{position:absolute;left:441px;top:27px;display:flex;gap:6px;white-space:nowrap}
.nav a{color:var(--white);font-size:11px;text-decoration:none;padding:3px 6px;letter-spacing:.3px}
.nav a.active{border:1px solid var(--white)}
.search{position:absolute;left:846px;top:25px;width:167px;height:24px;background:var(--white);display:flex;align-items:center;justify-content:space-between;padding:0 6px 0 8px;font-size:10px;color:#aaa}
.hero-copy{position:absolute;left:185px;top:178px;width:380px}
.hero-copy h1{color:var(--blue);font-size:30px;font-weight:700;margin-bottom:6px}
.hero-copy p{color:var(--blue);font-size:16px;font-weight:700;line-height:20px}
.btn-ghost{display:inline-block;margin-top:12px;border:1px solid var(--blue);color:var(--blue);background:var(--white);font-size:11px;padding:4px 16px}
.steps{position:absolute;left:185px;top:397px;width:830px;height:64px;background:rgba(20,22,26,.82);display:flex}
.step{flex:1;display:flex;align-items:center;gap:12px;padding-left:16px;color:var(--white);font-size:14px}
.step-num{width:30px;height:30px;border-radius:50%;background:var(--blue);display:flex;align-items:center;justify-content:center;font-weight:700;font-size:14px}

/* Sections */
.section-title{text-align:center;color:var(--ink);font-size:22px;font-weight:400;letter-spacing:.5px}
.title-rule{width:120px;height:2px;background:var(--ink);margin:10px auto 0}
.services{position:absolute;left:0;top:487px;width:1200px;height:385px}
.services .section-title{position:absolute;top:52px;width:1200px}
.services .title-rule{position:absolute;top:90px;left:540px;margin:0}
.feature-grid{top:122px;display:grid;grid-template-columns:430px 400px;row-gap:30px}
.feature{display:flex;gap:12px;height:58px}
.feature-icon{width:40px;height:40px;border-radius:50%;background:var(--blue);flex:none;display:flex;align-items:center;justify-content:center}
.feature h3{font-size:17px;font-weight:400;color:var(--ink);margin-bottom:5px}
.feature p{font-size:10.5px;line-height:13px;color:var(--text)}

.portfolio{position:absolute;left:0;top:872px;width:1200px;height:384px;background:linear-gradient(180deg,#e6e6e6,#f6f6f6 40%,#fafafa)}
.portfolio .section-title{position:absolute;top:40px;width:1200px}
.portfolio .title-rule{position:absolute;top:78px;left:540px;margin:0}
.cards{top:107px;height:218px;display:flex;gap:7px}
.card{flex:1;position:relative;background:var(--white)}
.card-photo{height:174px}
.card-caption{height:44px;background:#e4e4e4;font-size:11px;font-weight:700;color:var(--ink);padding:16px 8px 0}
.arrow{position:absolute;top:80px;width:22px;height:36px;background:#333;display:flex;align-items:center;justify-content:center}

.comments{position:absolute;left:0;top:1256px;width:1200px;height:526px}
.comments .comments-title{position:absolute;left:0;top:40px;width:1200px}
.comments .title-rule{position:absolute;top:78px;left:540px;margin:0}
.comments .clients-title{position:absolute;left:185px;top:360px;width:830px}
.testimonials{top:108px;display:flex;gap:12px}
.testimonial{flex:1;text-align:center}
.testimonial h4{font-size:12px;font-weight:400;color:var(--ink);margin-bottom:14px}
.t-band{height:64px;background:var(--soft);position:relative}
.t-quote{position:absolute;left:14px;top:18px;font-size:30px;color:#bbb;font-weight:700;line-height:1}
.t-photo{position:absolute;left:90px;top:0;width:90px;height:64px;background:linear-gradient(180deg,#d9c2b0,#b89680)}
.testimonial p{font-size:11px;line-height:13.5px;color:var(--text);margin-top:20px;padding:0 18px}
.divider{top:307px;height:24px}
.divider::before{content:"";position:absolute;left:0;right:0;top:12px;height:1px;background:var(--line)}
.divider svg{position:absolute;left:405px;top:2px;background:var(--white);padding:0 4px}
.logo-row{top:411px;display:flex;gap:12px}
.logo-box{flex:1;height:69px;border:1px solid var(--line);display:flex;align-items:center;justify-content:center;font-size:20px;font-weight:700;color:#cfcfcf}

.contact{position:absolute;left:0;top:1782px;width:1200px;height:243px;background:#f7f7f7}
.contact-col{position:absolute;top:42px;width:395px}
.contact-col h3{font-size:16px;font-weight:700;color:var(--ink);margin-bottom:6px}
.contact-col .rule{width:100%;height:1px;background:var(--line);margin-bottom:12px}
.contact-col p{font-size:11px;line-height:14px;margin-bottom:18px}
.field-row{display:flex;gap:8px}
.field{flex:1;height:24px;background:var(--white);border:1px solid var(--line);font-size:10px;color:#666;padding:6px 8px}
.field.tall{height:56px}
.btn{display:inline-block;background:var(--blue);color:var(--white);font-size:11px;padding:6px 16px;margin-top:12px}

.footer{position:absolute;left:0;top:2025px;width:1200px;height:231px;background:var(--footer);color:#bbb}
.footer-col{position:absolute;top:30px;width:260px}
.footer-col h3{font-size:17px;color:var(--white);font-weight:400;margin-bottom:22px}
.footer-col p{font-size:10.5px;line-height:14px}
.tags{display:flex;flex-wrap:wrap;gap:8px;width:260px}
.tag{background:var(--blue);color:var(--white);font-size:10px;padding:4px 16px}
.contact-list li{list-style:none;display:flex;gap:10px;font-size:10.5px;line-height:14px;margin-bottom:8px}
.contact-list svg{flex:none;margin-top:1px}
.copyright{position:absolute;left:0;top:2256px;width:1200px;height:52px;background:var(--footer-bottom);color:#888;font-size:10px;text-align:center;padding-top:20px}
</style>
</head>
<body>

<header class="hero">
  <div class="hero-photo" role="img" aria-label="Photograph of three business people in an office, smiling at the camera"></div>
  <div class="topbar"></div>
  <div class="brand"><span class="brand-dot"></span>EmberCrew Company</div>
  <nav class="nav">
    <a class="active" href="#">PRODUCTS</a><a href="#">PARTNERS</a><a href="#">COMPANY</a><a href="#">SUPPORT</a><a href="#">EVENTS</a>
  </nav>
  <div class="search">SEARCH
    <svg width="13" height="13" viewBox="0 0 13 13"><circle cx="5.5" cy="5.5" r="4" fill="none" stroke="#1a5d86" stroke-width="2"/><line x1="8.5" y1="8.5" x2="12" y2="12" stroke="#1a5d86" stroke-width="2"/></svg>
  </div>
  <div class="hero-copy">
    <h1>Welcome to our agency</h1>
    <p>Lorem ipsum dolor sit amet, consectetur adipiscing elit.</p>
    <span class="btn-ghost">more info</span>
  </div>
  <div class="steps">
    <div class="step"><span class="step-num">1</span>We are frendy</div>
    <div class="step"><span class="step-num">2</span>Planning</div>
    <div class="step"><span class="step-num">3</span>Development</div>
    <div class="step"><span class="step-num">4</span>24/7 Support</div>
  </div>
</header>

<section class="services">
  <h2 class="section-title">WHAT WE DO</h2>
  <div class="title-rule"></div>
  <div class="wrap feature-grid">
    <div class="feature"><span class="feature-icon"><svg width="20" height="20" viewBox="0 0 20 20"><rect x="2" y="3" width="16" height="11" fill="none" stroke="#fff" stroke-width="2"/><rect x="7" y="15" width="6" height="2" fill="#fff"/></svg></span><div><h3>Responsive Layout</h3><p>Lorem ipsum dolor sit amet, consectetur adipiscing elit. Suspendisse ut lorem at ex sodales auctor vitae eu ligula.</p></div></div>
    <div class="feature"><span class="feature-icon"><svg width="20" height="20" viewBox="0 0 20 20"><ellipse cx="10" cy="10" rx="8" ry="5" fill="none" stroke="#fff" stroke-width="2"/><circle cx="10" cy="10" r="2.5" fill="#fff"/></svg></span><div><h3>Retina Display Ready</h3><p>Lorem ipsum dolor sit amet, consectetur adipiscing elit. Suspendisse ut lorem at ex sodales auctor vitae eu ligula.</p></div></div>
    <div class="feature"><span class="feature-icon"><svg width="20" height="20" viewBox="0 0 20 20"><path d="M4 11a6 6 0 0 1 12 0" fill="none" stroke="#fff" stroke-width="2"/><rect x="3" y="10" width="3" height="5" fill="#fff"/><rect x="14" y="10" width="3" height="5" fill="#fff"/></svg></span><div><h3>Customer Support</h3><p>Lorem ipsum dolor sit amet, consectetur adipiscing elit. Suspendisse ut lorem at ex sodales auctor vitae eu ligula.</p></div></div>
    <div class="feature"><span class="feature-icon"><svg width="20" height="20" viewBox="0 0 20 20"><circle cx="6" cy="10" r="2.5" fill="#fff"/><circle cx="15" cy="5" r="2.5" fill="#fff"/><circle cx="15" cy="15" r="2.5" fill="#fff"/><path d="M6 10L15 5M6 10l9 5" stroke="#fff" stroke-width="1.5"/></svg></span><div><h3>Social Media Friendly</h3><p>Lorem ipsum dolor sit amet, consectetur adipiscing elit. Suspendisse ut lorem at ex sodales auctor vitae eu ligula.</p></div></div>
    <div class="feature"><span class="feature-icon"><svg width="20" height="20" viewBox="0 0 20 20"><rect x="5" y="3" width="10" height="5" fill="#fff"/><rect x="2" y="8" width="16" height="6" fill="none" stroke="#fff" stroke-width="2"/><rect x="5" y="13" width="10" height="4" fill="#fff"/></svg></span><div><h3>Print Design</h3><p>Lorem ipsum dolor sit amet, consectetur adipiscing elit. Suspendisse ut lorem at ex sodales auctor vitae eu ligula.</p></div></div>
    <div class="feature"><span class="feature-icon"><svg width="20" height="20" viewBox="0 0 20 20"><rect x="2" y="4" width="16" height="12" fill="none" stroke="#fff" stroke-width="2"/><path d="M4 14l4-5 3 3 2-2 3 4z" fill="#fff"/></svg></span><div><h3>Beautiful Gallery Sections</h3><p>Lorem ipsum dolor sit amet, consectetur adipiscing elit. Suspendisse ut lorem at ex sodales auctor vitae eu ligula.</p></div></div>
  </div>
</section>

<section class="portfolio">
  <h2 class="section-title">PORTFOLIO ITEMS</h2>
  <div class="title-rule"></div>
  <div class="wrap cards">
    <div class="card"><div class="card-photo" role="img" aria-label="Tablet showing a dashboard app on a desk" style="background:linear-gradient(135deg,#f1f1f1,#c9d4dc)"></div><div class="card-caption">Lorem ipsum dolor sit amet</div></div>
    <div class="card"><div class="card-photo" role="img" aria-label="Blue illustrated app interface mockup" style="background:linear-gradient(135deg,#2f7fc4,#1c5a99)"></div><div class="card-caption">Lorem ipsum dolor sit amet</div></div>
    <div class="card"><div class="card-photo" role="img" aria-label="Cardboard shipping boxes with labels" style="background:linear-gradient(135deg,#b79363,#7e5d38)"></div><div class="card-caption">Lorem ipsum dolor sit amet</div></div>
    <div class="card"><div class="card-photo" role="img" aria-label="Close-up of printed stationery with lettering" style="background:linear-gradient(135deg,#e8e2d6,#a89b86)"></div><div class="card-caption">Lorem ipsum dolor sit amet</div></div>
    <span class="arrow" style="left:-11px"><svg width="8" height="12" viewBox="0 0 8 12"><path d="M7 1L2 6l5 5" fill="none" stroke="#fff" stroke-width="2"/></svg></span>
    <span class="arrow" style="right:-11px"><svg width="8" height="12" viewBox="0 0 8 12"><path d="M1 1l5 5-5 5" fill="none" stroke="#fff" stroke-width="2"/></svg></span>
  </div>
</section>

<section class="comments">
  <h2 class="section-title comments-title">THE CLIENT'S COMMENTS</h2>
  <div class="title-rule"></div>
  <div class="wrap testimonials">
    <div class="testimonial"><h4>DANIEL</h4><div class="t-band"><span class="t-quote">&#8220;</span><div class="t-photo" role="img" aria-label="Portrait photo of the client"></div></div><p>Lorem ipsum dolor sit amet, consectetur adipiscing elit. Duis sed tristique nisl. Integer placerat ligula.</p></div>
    <div class="testimonial"><h4>LENA</h4><div class="t-band"><span class="t-quote">&#8220;</span><div class="t-photo" role="img" aria-label="Portrait photo of the client"></div></div><p>Lorem ipsum dolor sit amet, consectetur adipiscing elit. Duis sed tristique nisl. Integer placerat ligula.</p></div>
    <div class="testimonial"><h4>DANIEL</h4><div class="t-band"><span class="t-quote">&#8220;</span><div class="t-photo" role="img" aria-label="Portrait photo of the client"></div></div><p>Lorem ipsum dolor sit amet, consectetur adipiscing elit. Duis sed tristique nisl. Integer placerat ligula.</p></div>
  </div>
  <div class="wrap divider"><svg width="20" height="20" viewBox="0 0 20 20"><path d="M10 17L3 10a4 4 0 0 1 7-5 4 4 0 0 1 7 5z" fill="none" stroke="#555" stroke-width="1.6"/></svg></div>
  <h2 class="section-title clients-title">OUR CLIENTS</h2>
  <div class="wrap logo-row">
    <div class="logo-box">Lumaro</div><div class="logo-box">Novella</div><div class="logo-box">Chirpline</div>
    <div class="logo-box">Lumaro</div><div class="logo-box">Novella</div><div class="logo-box">Chirpline</div>
  </div>
</section>

<section class="contact">
  <div class="contact-col" style="left:185px">
    <h3>STAY WITH US</h3><div class="rule"></div>
    <p>Lorem ipsum dolor sit amet, consectetur adipiscing elit. Aenean commodo ligula eget dolor. Aenean massa.</p>
    <div class="field-row"><div class="field">Name</div><div class="field">Email</div></div>
    <span class="btn">SUBMIT</span>
  </div>
  <div class="contact-col" style="left:620px">
    <h3>SEND ANY QUERY</h3><div class="rule"></div>
    <div class="field-row"><div class="field">Name</div><div class="field">Email</div></div>
    <div class="field tall" style="margin-top:6px">Message</div>
    <span class="btn">SUBMIT</span>
  </div>
</section>

<footer class="footer">
  <div class="footer-col" style="left:185px">
    <h3>ABOUT US</h3>
    <p>Lorem ipsum dolor sit amet, consectetur adipiscing elit. Duis sed tristique nisl. Integer placerat ligula. Nam a tellus sed lorem ullamcorper luctus. Curabitur elementum tincidunt pretium.</p>
    <span class="btn">Read More</span>
  </div>
  <div class="footer-col" style="left:474px">
    <h3>POPULAR TAGS</h3>
    <div class="tags"><span class="tag">Lorem</span><span class="tag">Tellus</span><span class="tag">Ipsum dolor</span><span class="tag">Lorem</span><span class="tag">Suscipit</span></div>
  </div>
  <div class="footer-col" style="left:764px">
    <h3>CONTACT US</h3>
    <ul class="contact-list">
      <li><svg width="12" height="12" viewBox="0 0 12 12"><path d="M1 6l5-5 5 5v5H1z" fill="#ccc"/></svg>Harbor Lane 42, Northfield 5800</li>
      <li><svg width="12" height="12" viewBox="0 0 12 12"><path d="M3 1l2 3-1 1a6 6 0 0 0 3 3l1-1 3 2-1 2C5 11 1 7 1 2z" fill="#ccc"/></svg>+10 555 0142 18, +10 555 0199 27</li>
      <li><svg width="12" height="12" viewBox="0 0 12 12"><rect x="1" y="2.5" width="10" height="7" fill="#ccc"/><path d="M1 3l5 4 5-4" fill="none" stroke="#1d1f21"/></svg>hello@embercrew.example</li>
      <li><svg width="12" height="12" viewBox="0 0 12 12"><path d="M5 7l2-2M4 6L2.5 7.5a2 2 0 0 0 2 2L6 8M8 6l1.5-1.5a2 2 0 0 0-2-2L6 4" fill="none" stroke="#ccc" stroke-width="1.4"/></svg>www.embercrew.example</li>
    </ul>
  </div>
</footer>
<div class="copyright">Copyright © 2015 EmberCrew Company. All Rights Reserved.</div>

</body>
</html>
```